I need a business card to reflect my new qualifications.
Accredited Teacher, Accredited Valuer & Accredited Judge of Patchwork Quilting.
Fernbrook Lane Studio
47 Harlow Parade, Wodonga Vic 3690
0417 362 958 fernbrook@qlx.com.au

```html
<!DOCTYPE html>
<html lang="en">
<head>
<meta charset="utf-8">
<title>Fernbrook Lane Studio – Business Card</title>
<link rel="stylesheet" href="https://fonts.googleapis.com/css2?family=Jost:wght@400;500;600;800&display=swap">
<style>
  :root {
    --page: #ffffff;
    --orange: #e8781e;
    --orange-light: #f29a3a;
    --rust: #c9521f;
    --teal: #2f6f78;
    --plum: #7a3548;
    --slate: #4f5f86;
    --panel: #ffffff;
  }
  * { box-sizing: border-box; margin: 0; padding: 0; }
  html, body {
    width: 1200px;
    height: 1000px;
    overflow: hidden;
    background: var(--page);
    font-family: "Jost", sans-serif;
  }
  .canvas { position: relative; width: 1200px; height: 1000px; }
  .card {
    position: absolute;
    left: 269px;
    width: 662px;
    height: 405px;
    overflow: hidden;
  }
  .card--front { top: 81px; }
  .card--back { top: 537px; }
  .patchwork {
    position: absolute;
    inset: 0;
    background:
      radial-gradient(circle at 30% 40%, rgba(47,111,120,0.35), transparent 45%),
      radial-gradient(circle at 75% 65%, rgba(122,53,72,0.3), transparent 40%),
      linear-gradient(135deg, var(--orange-light), var(--orange) 45%, var(--rust));
  }
  .info-panel {
    position: absolute;
    left: 74px;
    top: 67px;
    width: 515px;
    height: 270px;
    background: var(--panel);
    text-align: center;
    color: var(--slate);
  }
  .studio-name {
    margin-top: 24px;
    font-weight: 800;
    font-size: 31px;
    letter-spacing: 0.5px;
    color: var(--orange);
    text-transform: uppercase;
    line-height: 1;
  }
  .person-name {
    margin-top: 22px;
    font-weight: 600;
    font-size: 26px;
    line-height: 1;
  }
  .credentials {
    margin-top: 10px;
    font-size: 19px;
    font-weight: 400;
    line-height: 1.3;
  }
  .contact {
    margin-top: 14px;
    font-size: 22px;
    font-weight: 400;
    line-height: 1.35;
  }
  .studio-name--large {
    position: absolute;
    left: 0;
    right: 0;
    top: 142px;
    text-align: center;
    font-weight: 800;
    font-size: 50px;
    line-height: 1.02;
    color: #ffffff;
    text-transform: uppercase;
  }
</style>
</head>
<body>
<main class="canvas">
  <section class="card card--front">
    <div class="patchwork" role="img" aria-label="Patchwork quilt pattern of orange, rust, teal and plum fabric squares set on point with stitched seams"></div>
    <div class="info-panel">
      <h1 class="studio-name">Fernbrook Lane Studio</h1>
      <h2 class="person-name">Helen Ashcombe</h2>
      <p class="credentials">Accredited Teacher, Accredited Valuer<br>&amp; Accredited Judge of Patchwork Quilting</p>
      <p class="contact">47 Harlow Parade, Wodonga Vic 3690<br>0417 362 958 • fernbrook@qlx.com.au</p>
    </div>
  </section>

  <section class="card card--back">
    <div class="patchwork" role="img" aria-label="Patchwork quilt pattern of orange, rust, teal and plum fabric squares set on point with stitched seams"></div>
    <p class="studio-name--large">Fernbrook Lane<br>Studio</p>
  </section>
</main>
</body>
</html>
```